WTF!!! We need a modern professional website for a business litigation law firm.

We need a modern, clean, professional and uncomplicated website for a new business trial and litigation law firm called "Hallorand Trial Firm PLLC". Website must be mobile optimized for iPad and smartphone. The law firm specializes in counseling and representing large corporations, small businesses and entrepreneurs in and out of the courtroom. Lawyers in the firm serve as Florida counsel and trial counsel to organizations facing claims involving product liability, premises liability, professional liability, vehicle and transportation liability, warranty claims, construction defects and delay claims, complex business disputes, commercial litigation and bid disputes in State and Federal Courts. The website is mainly to provide information about the firm, and should include sections describing the firm, identifying the Industries Served and Areas of Practice ," a separate page identifying the "Professionals", a separate page for "Resources & Advisories," and a traveling "Connect With Us" button a site visitor can click on that will launch an email to the Firm's general email account. The website should allow us to easily modify the content on these pages, and let us add/modify links to external information sources. We will not sell anything or take payments through the website. We do need to be able to easily upload and update photographs of attorneys and add new attorneys names/email hyperlinks as the firm grows. We would like to add developments in the law or success stories easily and quickly, such as through a blog page. On the "Connect With Us" page the website should have hyperlinks to email the Firm, and there should be hyperlinks to email each professional on the "Professionals" page. The website should be viewable on mobile devices without distortion. The law firm focuses on trial work and should have some imagery associated with courtrooms, but the overall theme of the site should be modern, clean, and communicate sophistication and strength. The website should be made in Wordpress. We have uploaded logo files for Hallorand Trial Firm.

Target Market(s)

Corporations and companies that are looking for legal representation. Other attorneys/legal industry.

Industry/Entity Type

Legal Industry

Coding

Coded - Design and coding required

Number of Pages Required

1 page

Font styles to use
Sans Serif

Requirements
Must have
• Simple, clean, sophisticated, modern website that includes the logo, watermark of logo, and the elements described above.
Nice to have
• Pictures of city scape, buildings, courtroom, team members.

```html
<!DOCTYPE html>
<html lang="en">
<head>
<meta charset="utf-8">
<title>Hallorand Trial Firm PLLC – Business Trial Advocacy</title>
<link href="https://fonts.googleapis.com/css2?family=Poppins:wght@300;400;500;600;700&display=swap" rel="stylesheet">
<style>
:root{
  --navy:#0f2a4a;
  --navy-deep:#0b2240;
  --gold:#a98b5a;
  --gold-dark:#8c7046;
  --ink:#1b1b1b;
  --text:#3c3c3c;
  --muted:#6b6b6b;
  --line:#d9d4cb;
  --card:#f4f3f0;
  --marble:#f2f1ef;
  --white:#ffffff;
}
*{box-sizing:border-box;margin:0;padding:0}
html,body{width:1200px;height:4747px;overflow:hidden}
body{position:relative;font-family:'Poppins',sans-serif;color:var(--text);background:var(--white)}
.abs{position:absolute}
a{color:inherit;text-decoration:none}
.btn{position:absolute;display:flex;align-items:center;justify-content:center;font-size:11px;letter-spacing:1.2px;text-transform:uppercase;height:35px}
.btn-navy{background:var(--navy);color:#fff;border:1px solid var(--gold)}
.btn-gold{background:var(--gold);color:#fff;border:1px solid var(--navy)}
.eyebrow{position:absolute;font-size:13px;letter-spacing:3.4px;text-transform:uppercase;color:var(--ink);display:flex;align-items:center;gap:16px}
.eyebrow .rule{display:block;width:80px;height:1px;background:var(--navy)}
.heading{position:absolute;font-weight:600;color:var(--ink);font-size:34px;line-height:1.17}
.heading .accent{color:var(--navy);font-weight:500}
.ph{position:absolute}

/* header */
.site-header{top:0;left:0;width:1200px;height:96px;background:#fff}
.brand{position:absolute;left:100px;top:22px;display:flex;align-items:center;gap:10px;font-weight:600;color:var(--ink)}
.brand-mark{width:18px;height:18px;background:var(--navy)}
.brand-name{font-size:16px;line-height:1.1;letter-spacing:.5px;text-transform:uppercase}
.call-box{left:875px;top:0;width:325px;height:64px;background:var(--gold);color:#fff}
.call-box .lbl{position:absolute;left:67px;top:12px;font-size:11px}
.call-box .num{position:absolute;left:67px;top:26px;font-size:22px;font-weight:600;font-style:italic}
.call-box .ico{position:absolute;left:22px;top:16px;width:30px;height:30px;border-radius:50%;background:var(--navy-deep);display:flex;align-items:center;justify-content:center}
.main-nav{left:295px;top:64px;width:905px;height:39px;background:var(--navy-deep);display:flex;align-items:center;gap:36px;padding-left:36px;color:#fff;font-size:10.5px;text-transform:uppercase}

/* hero */
.hero{top:96px;left:0;width:1200px;height:531px}
.hero-photo{left:0;top:0;width:1200px;height:531px;background:linear-gradient(180deg,#7e6f5c 0%,#b4a58d 30%,#d8d0c3 55%,#ece9e4 80%,#f3f2f0 100%)}
.hero-title{left:0;width:1200px;top:214px;text-align:center;color:var(--ink);font-size:44px;line-height:1.17;text-transform:uppercase}
.hero-title .l1{font-weight:300}
.hero-title .l2{font-weight:600}
.hero-sub{left:0;width:1200px;top:326px;text-align:center;font-size:12.5px;line-height:1.55;color:var(--ink)}

.marble{background:linear-gradient(160deg,#f7f6f4 0%,#eceae7 40%,#f5f4f2 70%,#e9e7e3 100%)}

/* about */
.about{top:627px;left:0;width:1200px;height:582px}
.about-text{left:100px;top:135px;width:500px;font-size:12.3px;line-height:1.62;color:var(--ink)}
.about-text p{margin-bottom:14px}

/* practice */
.practice{top:1209px;left:0;width:1200px;height:861px;background:#fff}
.card{position:absolute;width:320px;height:252px;background:var(--card);padding:12px}
.card-inner{width:100%;height:100%;border:1px solid #7a7a7a;background:#fff;text-align:center;padding-top:20px}
.card-inner svg{display:block;margin:0 auto 6px}
.card h3{font-size:14.5px;font-weight:600;color:var(--ink);line-height:1.3}
.card p{font-size:12.5px;line-height:1.48;color:var(--text);margin:10px auto 0;width:250px}
.card .more{display:inline-block;margin-top:10px;font-size:11.5px;letter-spacing:1px;color:var(--gold);text-decoration:underline}

/* team */
.team{top:2070px;left:0;width:1200px;height:409px;background:linear-gradient(90deg,#e8e5df 0%,#f6f5f2 30%,#f8f7f5 70%,#e4e0d9 100%)}
.member{position:absolute;top:180px;width:242px;height:221px;background:#fff}
.member .photo{position:absolute;left:0;top:0;width:100%;height:168px}
.member .name{position:absolute;left:0;top:168px;width:100%;height:53px;padding-left:22px;display:flex;align-items:center;font-size:14px;font-weight:600;color:var(--ink)}
.member.active .name{background:var(--gold);color:#fff;justify-content:space-between;padding-right:22px}

/* industries */
.industries{top:2479px;left:0;width:1200px;height:728px}
.tile{position:absolute;top:328px;width:194px;height:273px}
.tile span{position:absolute;left:14px;bottom:20px;color:#fff;font-size:14px;font-weight:500;line-height:1.3}

/* blog */
.blog{top:3207px;left:0;width:1200px;height:581px;background:#fff}
.post{position:absolute;top:151px;width:324px}
.post .img{width:100%;height:199px}
.post .meta{margin-top:22px;font-size:11px;letter-spacing:.5px;color:var(--navy);text-transform:uppercase}
.post h4{margin-top:8px;font-size:14.5px;font-weight:600;line-height:1.45;color:var(--ink)}
.post p{margin-top:8px;font-size:12px;line-height:1.55;color:var(--text)}
.post .more{display:inline-block;margin-top:10px;font-size:11.5px;letter-spacing:1px;color:var(--gold);text-decoration:underline}

/* contact */
.contact{top:3788px;left:0;width:1200px;height:500px;background:linear-gradient(90deg,#e6e3dd 0%,#f7f6f4 35%,#f8f7f5 65%,#e3dfd8 100%)}
.field{position:absolute;height:36px;background:#fff;border:1px solid #bdbdbd;font-size:10px;color:var(--muted);padding:10px 12px}

/* footer */
.footer{top:4147px;left:0;width:1200px;height:600px}
.foot-brand{left:0;width:1200px;top:200px;text-align:center;color:#fff;font-weight:600;font-size:30px;letter-spacing:1px;text-transform:uppercase;line-height:1.2}
.foot-nav{left:140px;width:920px;top:342px;display:flex;justify-content:space-between;color:#fff;font-size:13px;text-transform:uppercase}
.foot-line{left:140px;width:920px;height:1px;background:rgba(255,255,255,.55)}
.foot-contact{top:420px;color:#fff;font-size:19px;line-height:1.25;display:flex;align-items:center;gap:14px}
.foot-ico{width:32px;height:32px;border-radius:50%;background:#fff;display:flex;align-items:center;justify-content:center;flex:none}
.foot-div{top:412px;width:1px;height:62px;background:rgba(255,255,255,.55)}
.copy{left:0;width:1200px;top:551px;text-align:center;color:#fff;font-size:12px;letter-spacing:.6px}
</style>
</head>
<body>

<!-- Header -->
<header class="abs site-header">
  <div class="brand"><span class="brand-mark"></span><span class="brand-name">Hallorand<br>Trial Firm</span></div>
  <div class="abs call-box">
    <span class="ico"><svg width="14" height="14" viewBox="0 0 24 24" fill="#fff"><path d="M6.6 10.8a15.1 15.1 0 0 0 6.6 6.6l2.2-2.2c.3-.3.7-.4 1-.2 1.1.4 2.3.6 3.6.6.6 0 1 .4 1 1V20c0 .6-.4 1-1 1A17 17 0 0 1 3 4c0-.6.4-1 1-1h3.5c.6 0 1 .4 1 1 0 1.3.2 2.5.6 3.6.1.3 0 .7-.2 1z"/></svg></span>
    <span class="lbl">Free Consultation :</span>
    <span class="num">123-456-7890</span>
  </div>
  <nav class="abs main-nav">
    <a>Home</a><a>About Us</a><a>Areas of Practice</a><a>Industries Served</a><a>Resources</a><a>Professionals</a><a>Connect With Us</a>
  </nav>
</header>

<!-- Hero -->
<section class="abs hero">
  <div class="ph hero-photo" role="img" aria-label="Grand courthouse hall with stone columns and warm lit windows"></div>
  <h1 class="abs hero-title"><span class="l1">Trial Advocacy For</span><br><span class="l2">Modern Business Challenges.</span></h1>
  <p class="abs hero-sub">We deliver exceptional legal counsel and representation to corporations,<br>small businesses, and entrepreneurs throughout Florida.</p>
  <a class="btn btn-navy" style="left:374px;top:385px;width:240px">Schedule a Consultation</a>
  <a class="btn btn-gold" style="left:624px;top:385px;width:200px">Learn More About Us</a>
</section>

<!-- About -->
<section class="abs about marble">
  <div class="eyebrow" style="left:100px;top:135px"><span>About Us</span><span class="rule"></span></div>
  <h2 class="heading" style="left:100px;top:160px">Sophisticated Legal Counsel<br>for <span class="accent">Modern Challenges.</span></h2>
  <div class="abs about-text" style="top:255px">
    <p>At Hallorand Trial Firm PLLC, we provide strategic and results-driven legal representation for businesses of all sizes. Our attorneys specialize in high-stakes litigation, offering expert counsel in complex disputes across industries. With a commitment to excellence, we advocate for our clients in and out of the courtroom, ensuring sophisticated and effective legal solutions.</p>
    <p>We are committed to delivering sophisticated legal solutions tailored to the needs of modern businesses. Whether in the courtroom or at the negotiation table, our goal is to provide effective, results-driven advocacy that helps our clients succeed.</p>
  </div>
  <a class="btn btn-gold" style="left:100px;top:470px;width:200px">Learn More About Us</a>
  <div class="abs" style="left:660px;top:145px;width:440px;height:355px;border:2px solid var(--navy)"></div>
  <div class="abs" style="left:636px;top:128px;width:438px;height:355px;background:#fff;box-shadow:0 2px 8px rgba(0,0,0,.15)"></div>
  <div class="ph" style="left:636px;top:128px;width:438px;height:350px;background:linear-gradient(135deg,#6b4a36 0%,#8b94a0 45%,#3e5d74 70%,#2b3340 100%)" role="img" aria-label="Business team shaking hands across a meeting table in an office"></div>
</section>

<!-- Hero V edge -->
<svg class="abs" style="left:0;top:480px" width="1200" height="150" viewBox="0 0 1200 150">
  <polygon points="0,0 600,118 1200,0 1200,150 0,150" fill="#f4f3f1"/>
  <polygon points="0,-14 600,120 1200,-14 1200,6 600,147 0,6" fill="var(--navy)"/>
</svg>

<!-- Practice areas -->
<section class="abs practice">
  <div class="eyebrow" style="left:0;width:1200px;top:75px;justify-content:center"><span class="rule"></span><span>Expertise Across Key Practice Areas.</span><span class="rule"></span></div>
  <h2 class="heading" style="left:0;width:1200px;top:107px;text-align:center">Comprehensive Litigation &amp;<br><span class="accent">Business Advocacy.</span></h2>

  <div class="card" style="left:100px;top:210px"><div class="card-inner">
    <svg width="46" height="46" viewBox="0 0 46 46" fill="none" stroke="#a98b5a" stroke-width="1.6"><rect x="6" y="14" width="34" height="24" rx="2"/><path d="M17 14v-5h12v5M6 24h34"/><rect x="20" y="21" width="6" height="6"/></svg>
    <h3>Business &amp;<br>Commercial Litigation</h3>
    <p>Handling disputes involving contracts, partnerships, shareholder rights, fraud, and business torts.</p>
    <a class="more">READ MORE</a></div></div>
  <div class="card" style="left:440px;top:210px"><div class="card-inner">
    <svg width="46" height="46" viewBox="0 0 46 46" fill="none" stroke="#a98b5a" stroke-width="1.6"><path d="M8 15l15-7 15 7v17l-15 7-15-7z"/><path d="M8 15l15 7 15-7M23 22v17"/><circle cx="33" cy="33" r="6"/></svg>
    <h3>Product<br>Liability Defense</h3>
    <p>Representing property owners, businesses in claims related to accidents, security issues, negligence.</p>
    <a class="more">READ MORE</a></div></div>
  <div class="card" style="left:780px;top:210px"><div class="card-inner">
    <svg width="46" height="46" viewBox="0 0 46 46" fill="none" stroke="#a98b5a" stroke-width="1.6"><circle cx="21" cy="15" r="6"/><path d="M9 38c0-8 5-13 12-13s12 5 12 13z"/><path d="M30 10l8 3v7c0 5-4 8-8 9-4-1-8-4-8-9"/></svg>
    <h3>Professional<br>Liability Defense</h3>
    <p>Handling disputes involving contracts, partnerships, shareholder rights, fraud, and business torts.</p>
    <a class="more">READ MORE</a></div></div>
  <div class="card" style="left:100px;top:479px"><div class="card-inner">
    <svg width="46" height="46" viewBox="0 0 46 46" fill="none" stroke="#a98b5a" stroke-width="1.6"><circle cx="23" cy="23" r="14"/><circle cx="23" cy="23" r="5"/><path d="M23 5v6M23 35v6M5 23h6M35 23h6"/></svg>
    <h3>Construction<br>Defect &amp; Delay Claims</h3>
    <p>Handling disputes involving contracts, partnerships, shareholder rights, fraud, and business torts.</p>
    <a class="more">READ MORE</a></div></div>
  <div class="card" style="left:440px;top:479px"><div class="card-inner">
    <svg width="46" height="46" viewBox="0 0 46 46" fill="none" stroke="#a98b5a" stroke-width="1.6"><rect x="5" y="18" width="22" height="14"/><path d="M27 22h8l5 5v5H27"/><circle cx="12" cy="34" r="3"/><circle cx="33" cy="34" r="3"/><path d="M14 8l6 6M20 8l-6 6"/></svg>
    <h3>Transportation<br>&amp; Vehicle Liability</h3>
    <p>Handling disputes involving contracts, partnerships, shareholder rights, fraud, and business torts.</p>
    <a class="more">READ MORE</a></div></div>
  <div class="card" style="left:780px;top:479px"><div class="card-inner">
    <svg width="46" height="46" viewBox="0 0 46 46" fill="none" stroke="#a98b5a" stroke-width="1.6"><rect x="12" y="6" width="24" height="32"/><path d="M17 14h14M17 20h14M17 26h10"/><circle cx="12" cy="34" r="5"/></svg>
    <h3>Bid Protests &amp;<br>Government Contracts</h3>
    <p>Challenging or defending contract awards in government procurement disputes.</p>
    <a class="more">READ MORE</a></div></div>

  <a class="btn btn-gold" style="left:522px;top:763px;width:156px">Discover More</a>
</section>

<!-- Team -->
<section class="abs team">
  <div class="eyebrow" style="left:100px;top:60px"><span>Meet Our Team</span></div>
  <h2 class="heading" style="left:100px;top:85px">Experienced Litigators.<br><span class="accent">Proven Advocates</span></h2>
  <a class="btn btn-navy" style="left:864px;top:99px;width:236px">Schedule a Consultation</a>

  <div class="member" style="left:100px"><div class="photo" style="background:linear-gradient(160deg,#c9c6c0,#5b5e63 70%,#2b2d31)" role="img" aria-label="Portrait of attorney Daniel Okafor"></div><div class="name">Daniel Okafor</div></div>
  <div class="member" style="left:353px"><div class="photo" style="background:linear-gradient(160deg,#e6e4e0,#9c9288 60%,#2d2f35)" role="img" aria-label="Portrait of attorney Elias Brandt"></div><div class="name">Elias Brandt</div></div>
  <div class="member active" style="left:606px"><div class="photo" style="background:linear-gradient(160deg,#d7b98d,#9a7a55 55%,#2a2a2e)" role="img" aria-label="Portrait of attorney Maren Castell"></div><div class="name"><span>Maren Castell</span><svg width="18" height="10" viewBox="0 0 18 10" fill="none" stroke="#fff" stroke-width="1.4"><path d="M0 5h16M12 1l4 4-4 4"/></svg></div></div>
  <div class="member" style="left:859px"><div class="photo" style="background:linear-gradient(160deg,#c8a27a,#e7e3dc 45%,#3a3d45)" role="img" aria-label="Portrait of attorney Victor Lindqvist"></div><div class="name">Victor Lindqvist</div></div>
</section>

<!-- Industries -->
<section class="abs industries marble">
  <div class="eyebrow" style="left:0;width:1200px;top:195px;justify-content:center"><span class="rule"></span><span>Industries We Serve</span><span class="rule"></span></div>
  <h2 class="heading" style="left:0;width:1200px;top:222px;text-align:center">Serving Businesses Across<br><span class="accent">Diverse Industries.</span></h2>

  <svg class="abs" style="left:64px;top:457px" width="20" height="14" viewBox="0 0 20 14" fill="none" stroke="#333" stroke-width="1.4"><path d="M19 7H2M7 1L1 7l6 6"/></svg>
  <svg class="abs" style="left:1116px;top:457px" width="20" height="14" viewBox="0 0 20 14" fill="none" stroke="#333" stroke-width="1.4"><path d="M1 7h17M13 1l6 6-6 6"/></svg>

  <div class="tile" style="left:100px;background:linear-gradient(180deg,#8c9098 0%,#6a6f78 45%,#183a5f 100%)" role="img" aria-label="Construction worker on a building site"><span>Construction</span></div>
  <div class="tile" style="left:303px;background:linear-gradient(180deg,#4f7593 0%,#3a6283 45%,#133659 100%)" role="img" aria-label="Support worker with headset at a computer"><span>Technology &amp;<br>Software</span></div>
  <div class="tile" style="left:503px;background:linear-gradient(180deg,#9ea3aa 0%,#6c7a8a 45%,#143659 100%)" role="img" aria-label="Retail staff reviewing a folder in a shop"><span>Retail &amp; Hospitality</span></div>
  <div class="tile" style="left:704px;background:linear-gradient(180deg,#8d95a0 0%,#6e6670 45%,#163a5e 100%)" role="img" aria-label="Bus inside a transport depot"><span>Transportation &amp;<br>Logistics</span></div>
  <div class="tile" style="left:906px;background:linear-gradient(180deg,#b2b3b4 0%,#6f747b 45%,#143659 100%)" role="img" aria-label="Businesswoman reviewing real estate documents"><span>Real Estate &amp;<br>Development</span></div>

  <a class="btn btn-gold" style="left:522px;top:626px;width:156px">Discover More</a>
</section>

<!-- Team V edge -->
<svg class="abs" style="left:0;top:2466px" width="1200" height="155" viewBox="0 0 1200 155">
  <polygon points="0,0 1200,0 1200,14 600,138 0,14" fill="var(--navy)"/>
  <polygon points="0,0 1200,0 1200,2 600,108 0,2" fill="#eeece8"/>
</svg>

<!-- Blog -->
<section class="abs blog">
  <div class="eyebrow" style="left:100px;top:54px"><span>Resources &amp; Advisories</span><span class="rule"></span></div>
  <h2 class="heading" style="left:100px;top:88px">Our Blog</h2>
  <a class="btn btn-navy" style="left:908px;top:70px;width:192px;height:34px;border-color:var(--gold)">View All Resources.</a>

  <article class="post" style="left:100px"><div class="img" style="background:linear-gradient(135deg,#7a3d27,#c9b9a4 45%,#2f3238)" role="img" aria-label="Agent handing house keys and documents to a client"></div><div class="meta">30Jan, 2025 by John Deo</div><h4>Lorem Ipsum is simply dummy text of the printing and typesetting industry.</h4><p>Handling disputes involving contracts,<br>partnerships, shareholder rights, fraud,<br>and business torts.</p><a class="more">READ MORE</a></article>
  <article class="post" style="left:437px"><div class="img" style="background:linear-gradient(135deg,#6b4a34,#c9ccd0 45%,#3b3f47)" role="img" aria-label="Colleagues reviewing papers in an office hallway"></div><div class="meta">30Jan, 2025 by John Deo</div><h4>Lorem Ipsum is simply dummy text of the printing and typesetting industry.</h4><p>Handling disputes involving contracts,<br>partnerships, shareholder rights, fraud,<br>and business torts.</p><a class="more">READ MORE</a></article>
  <article class="post" style="left:776px"><div class="img" style="background:linear-gradient(90deg,#5a3a26 0%,#7a5236 25%,#eeeae4 40%,#d9d3cb 80%,#6a4a34 100%)" role="img" aria-label="Hand stamping a delayed notice on paper"></div><div class="meta">30Jan, 2025 by John Deo</div><h4>Lorem Ipsum is simply dummy text of the printing and typesetting industry.</h4><p>Handling disputes involving contracts,<br>partnerships, shareholder rights, fraud,<br>and business torts.</p><a class="more">READ MORE</a></article>
</section>

<!-- Contact -->
<section class="abs contact">
  <div class="eyebrow" style="left:0;width:1200px;top:72px;justify-content:center"><span class="rule"></span><span>Contact Us</span><span class="rule"></span></div>
  <h2 class="heading" style="left:0;width:1200px;top:100px;text-align:center">Get In Touch With US</h2>
  <div class="field" style="left:275px;top:165px;width:332px">First Name</div>
  <div class="field" style="left:615px;top:165px;width:332px">Last Name</div>
  <div class="field" style="left:275px;top:211px;width:332px">Email</div>
  <div class="field" style="left:615px;top:211px;width:332px">Phone</div>
  <div class="field" style="left:275px;top:257px;width:672px;height:96px">Message</div>
</section>

<!-- Footer -->
<footer class="abs footer">
  <svg class="abs" style="left:0;top:0" width="1200" height="600" viewBox="0 0 1200 600">
    <polygon points="0,0 600,128 1200,0 1200,600 0,600" fill="var(--navy-deep)"/>
    <polygon points="0,0 600,128 1200,0 1200,6 600,140 0,6" fill="var(--gold)"/>
  </svg>
  <a class="btn btn-navy" style="left:540px;top:41px;width:120px;height:34px">Send Now</a>
  <div class="abs foot-brand">Hallorand<br>Trial Firm</div>
  <nav class="abs foot-nav"><a>Home</a><a>About Us</a><a>Areas of Practice</a><a>Industries Served</a><a>Resources</a><a>Professionals</a><a>Connect With Us</a></nav>
  <div class="abs foot-line" style="top:386px"></div>
  <div class="abs foot-contact" style="left:168px;top:430px"><span class="foot-ico"><svg width="16" height="16" viewBox="0 0 24 24" fill="#0b2240"><path d="M6.6 10.8a15.1 15.1 0 0 0 6.6 6.6l2.2-2.2c.3-.3.7-.4 1-.2 1.1.4 2.3.6 3.6.6.6 0 1 .4 1 1V20c0 .6-.4 1-1 1A17 17 0 0 1 3 4c0-.6.4-1 1-1h3.5c.6 0 1 .4 1 1 0 1.3.2 2.5.6 3.6.1.3 0 .7-.2 1z"/></svg></span>123-456-7890</div>
  <div class="abs foot-div" style="left:374px"></div>
  <div class="abs foot-contact" style="left:404px;top:410px;align-items:flex-start"><span class="foot-ico" style="margin-top:2px"><svg width="14" height="16" viewBox="0 0 14 18" fill="none" stroke="#0b2240" stroke-width="1.6"><path d="M7 17s6-6 6-10A6 6 0 0 0 1 7c0 4 6 10 6 10z"/><circle cx="7" cy="7" r="2"/></svg></span><span>Lorem Ipsum is simply<br>dummy &nbsp;industry.<br>115 56 simpl industry.</span></div>
  <div class="abs foot-div" style="left:691px"></div>
  <div class="abs foot-contact" style="left:718px;top:430px"><span class="foot-ico"><svg width="16" height="12" viewBox="0 0 16 12" fill="none" stroke="#0b2240" stroke-width="1.4"><rect x="1" y="1" width="14" height="10" rx="1"/><path d="M1 2l7 5 7-5"/></svg></span>info@hallorandtrialfirm.com</div>
  <div class="abs foot-line" style="top:516px"></div>
  <p class="abs copy">© Copyright All Right Reserved Hallorand Trial Firm PLLC 2025</p>
</footer>

</body>
</html>
```